Upbeat Accouting Package Flyer

I am looking for a 1 page (front, or front and back) flyer that will become our marketing for our accounting services. We are looking for something a little different and we are catering to the small retail shop owners. We have 3 accounting packages we would like to display and then some add-ons. I have included our logo that must be included in the design. I have uploaded the accounting package information as well.
Target Market(s)
Small Retail Shop Owners
Industry/Entity Type
Accounting
Colors
Designer to choose colors to be used in the design.
Requirements
Must have
- A casual feel. We are not your typical accountants who are very professional and "stuffy". I want it to feel like we are all family.
Nice to have
- I would like to incorporate some sort of retail theme.
- We have a couple of taglines we like to use and it would be great if they could be included. They are "We know you CAN do the accounting, but do you WANT to?" and "We allow you to get back to what's important."
Should not have
- Typical stock accounting photos of people shaking hands, large office buildings, etc.

```html
<!DOCTYPE html>
<html lang="en">
<head>
<meta charset="utf-8">
<title>Brightledger Accounting Packages Flyer</title>
<link rel="stylesheet" href="https://fonts.googleapis.com/css2?family=Open+Sans:wght@400;600;700;800&display=swap">
<style>
  :root {
    --backdrop: #acd5df;
    --ink: #141414;
    --panel: #1c1d1f;
    --cyan: #1fb8d8;
    --white: #ffffff;
  }
  * { box-sizing: border-box; margin: 0; padding: 0; }
  html, body { width: 1200px; height: 893px; overflow: hidden; }
  body {
    background: var(--backdrop);
    font-family: "Open Sans", Arial, sans-serif;
    display: flex; align-items: center; justify-content: center;
  }
  .flyer {
    position: relative; width: 640px; height: 850px;
    background: var(--panel); overflow: hidden;
    box-shadow: 0 6px 24px rgba(0,0,0,.18);
  }
  .hero {
    position: absolute; left: 0; top: 0; width: 100%; height: 300px;
    background:
      radial-gradient(ellipse at 25% 75%, #0b5f84 0%, transparent 55%),
      radial-gradient(ellipse at 80% 20%, #8fdcf0 0%, transparent 55%),
      linear-gradient(135deg, #1a9cc6 0%, #3fb9dc 50%, #9bdcec 100%);
  }
  .hero-stripe { position: absolute; left: 240px; right: 0; top: 0; height: 12px; background: var(--cyan); }
  .hero-stripe::after { content: ""; position: absolute; left: 0; right: 0; top: 12px; height: 3px; background: var(--white); }
  .brand-tab {
    position: absolute; left: 0; top: 118px; width: 250px; height: 68px;
    background: var(--ink); border: 3px solid var(--white); border-left: none;
    display: flex; flex-direction: column; justify-content: center; padding-left: 22px;
  }
  .brand-name { color: var(--white); font-weight: 700; font-size: 34px; line-height: 1; letter-spacing: .5px; }
  .brand-sub { color: var(--cyan); font-weight: 400; font-size: 10px; letter-spacing: .6px; margin-top: 4px; text-transform: uppercase; }
  .tagline {
    position: absolute; right: 34px; top: 140px; text-align: right;
    color: var(--white); font-weight: 600; font-size: 22px; line-height: 1.05;
    text-shadow: 0 1px 3px rgba(0,0,0,.25);
  }
  .tagline strong { font-weight: 800; font-size: 36px; }
  .packages-title {
    position: absolute; left: 26px; top: 314px; width: 310px;
    color: var(--cyan); font-weight: 700; font-size: 26px; line-height: 1.2;
  }
  .package { position: absolute; left: 26px; width: 310px; color: var(--white); }
  .package h2, .package-relax h2 { color: var(--cyan); font-size: 19px; font-weight: 700; line-height: 1.2; margin-bottom: 2px; }
  .features { list-style: none; font-size: 11px; line-height: 1.18; }
  .features li { position: relative; padding-left: 12px; margin-bottom: 1px; }
  .features li::before {
    content: ""; position: absolute; left: 0; top: 4px; width: 6px; height: 6px;
    border-radius: 50%; background: var(--cyan);
  }
  .package-develop { top: 362px; }
  .package-grow { top: 498px; }
  .package-relax {
    position: absolute; left: 354px; top: 282px; width: 272px;
    background: var(--white); color: var(--ink); padding: 14px 16px 15px;
    outline: 2px dashed #555; outline-offset: -7px;
  }
  .options {
    position: absolute; left: 354px; top: 574px; width: 272px;
    background: var(--ink); color: var(--white); padding: 14px 16px 15px;
    outline: 2px dashed var(--cyan); outline-offset: -7px;
  }
  .options h2 { color: var(--cyan); font-size: 19px; font-weight: 700; line-height: 1.2; margin-bottom: 6px; text-align: center; }
  .options-table { width: 100%; border-collapse: collapse; font-size: 11px; line-height: 1.25; }
  .options-table td { vertical-align: top; padding: 1px 0; }
  .options-table td:first-child { width: 42%; }
  .options-table .bullet { display: inline-block; width: 6px; height: 6px; border-radius: 50%; background: var(--cyan); margin-right: 6px; vertical-align: 1px; }
  .contact-band {
    position: absolute; left: 0; right: 0; bottom: 0; height: 112px; background: var(--cyan);
  }
  .contact-band::before { content: ""; position: absolute; left: 0; right: 0; top: 0; height: 4px; background: var(--white); }
  .contact-info {
    position: absolute; left: 28px; top: 14px; color: var(--ink); font-style: normal;
    font-size: 12.5px; font-weight: 600; line-height: 1.3;
  }
  .web-box {
    position: absolute; left: 0; bottom: 0; width: 300px; height: 38px; background: var(--white);
    display: flex; align-items: center; padding-left: 28px;
    color: var(--ink); font-weight: 700; font-size: 17px;
  }
</style>
</head>
<body>
  <main class="flyer">
    <div class="hero" role="img" aria-label="Close-up photo of scattered blue three-dimensional numbers"></div>
    <div class="hero-stripe"></div>

    <div class="brand-tab">
      <span class="brand-name">brightledger</span>
      <span class="brand-sub">Tax and Accounting Inc.</span>
    </div>

    <p class="tagline">We know you <strong>CAN</strong><br>do the accounting,<br>but do you <strong>WANT</strong> to?</p>

    <h1 class="packages-title">Accounting Packages:</h1>

    <section class="package package-develop">
      <h2>Develop:</h2>
      <ul class="features">
        <li>$300/mo when paid annually; $325/mo billed monthly</li>
        <li>LedgerCloud Online subscription</li>
        <li>Free accounting setup</li>
        <li>Weekly transaction processing</li>
        <li>Monthly account reconciliation (up to 2 accounts)</li>
        <li>Monthly financial statements by the 15th of the month</li>
      </ul>
    </section>

    <section class="package package-grow">
      <h2>Grow:</h2>
      <ul class="features">
        <li>$550/mo billed annually; $575/mo billed monthly</li>
        <li>LedgerCloud Online subscription</li>
        <li>Free accounting setup</li>
        <li>Weekly transaction processing</li>
        <li>Monthly account reconciliation (up to 4 accounts)</li>
        <li>Monthly financial statements by the 10th of the month</li>
        <li>Client portal access for document sharing</li>
        <li>1 Custom Report</li>
        <li>Accounts Payable</li>
        <li>Monthly Scorecard (customized metric tracking for your business)</li>
      </ul>
    </section>

    <section class="package-relax">
      <h2>Relax (We've Got This):</h2>
      <ul class="features">
        <li>$850/mo billed annually; $875/mo billed monthly</li>
        <li>LedgerCloud Online subscription</li>
        <li>Free accounting setup</li>
        <li>Weekly transaction processing</li>
        <li>Monthly account reconciliation (up to 5-10 accounts)</li>
        <li>Monthly financial statements by the 5th of the month</li>
        <li>Client portal access for document sharing</li>
        <li>2 Custom Reports</li>
        <li>Accounts Payable</li>
        <li>Invoicing and accounts receivable</li>
        <li>Weekly Scorecard (customized metric tracking for your business)</li>
      </ul>
    </section>

    <section class="options">
      <h2>Additional Options</h2>
      <table class="options-table">
        <tr><td><span class="bullet"></span>Payroll</td><td>1-10 employees $85/mo;<br>11-30 employees $175/mo</td></tr>
        <tr><td><span class="bullet"></span>Sales tax</td><td>$30/mo per state</td></tr>
        <tr><td><span class="bullet"></span>Corporate taxes</td><td>$50/mo</td></tr>
        <tr><td><span class="bullet"></span>Owner taxes</td><td>$25/mo</td></tr>
      </table>
    </section>

    <footer class="contact-band">
      <address class="contact-info">
        (555) 014-2270<br>
        4410 W. Maple Street Fairview, KS 66000<br>
        hello@brightledger-co.com
      </address>
      <div class="web-box">www.brightledgerco.com</div>
    </footer>
  </main>
</body>
</html>
```